Business Card *

A business card design
Use the logo uploaded in the brief page.
You may use placeholders in your design layouts.
I will provide the actual business card details to the winning designer.

Logo
Place for contact info (name, title, phone, email, etc)

Requirements
Must have
• Logo

```html
<!DOCTYPE html>
<html lang="en">
<head>
<meta charset="utf-8">
<title>Ridgeline Agriculture and Industry – Business Card</title>
<link rel="stylesheet" href="https://fonts.googleapis.com/css2?family=Montserrat:wght@400;500;700&family=Open+Sans:wght@400;600&display=swap">
<style>
  :root {
    --backdrop: #3b3b39;
    --card: #151515;
    --card-edge: #1d1d1d;
    --pattern: #1b1b1b;
    --silver: #c9c9c9;
    --text-light: #d6d6d6;
    --green: #5cbf5f;
  }
  * { box-sizing: border-box; margin: 0; padding: 0; }
  html, body {
    width: 1200px; height: 824px; overflow: hidden;
    background: var(--backdrop);
  }
  .canvas {
    position: relative; width: 1200px; height: 824px;
    display: flex; align-items: center; justify-content: center; gap: 60px;
  }
  .card {
    position: relative; width: 500px; height: 286px;
    background: var(--card);
    border: 1px solid var(--card-edge);
    border-radius: 4px;
    box-shadow: 0 12px 30px rgba(0,0,0,.45);
    overflow: hidden;
  }

  /* Front */
  .card-front__pattern {
    position: absolute; inset: 0;
    background: linear-gradient(135deg, var(--pattern), var(--card) 70%, #1f1f1f);
  }
  .brand {
    position: absolute; display: flex; align-items: center; gap: 10px;
    font-family: "Montserrat", sans-serif; font-weight: 700;
    color: var(--silver); text-transform: uppercase; line-height: 1.2;
    white-space: nowrap;
  }
  .brand__dot {
    flex: none; border-radius: 50%; border: 3px solid var(--silver);
  }
  .card-front .brand { right: 40px; top: 50%; transform: translateY(-50%); font-size: 17px; letter-spacing: 1px; }
  .card-front .brand__dot { width: 54px; height: 54px; }

  /* Back */
  .card-back .brand { left: 28px; top: 96px; font-size: 11px; letter-spacing: .4px; }
  .card-back .brand__dot { width: 34px; height: 34px; border-width: 2.5px; }

  .contact {
    position: absolute; left: 300px; top: 150px;
    font-family: "Open Sans", sans-serif; color: var(--text-light);
  }
  .contact__name {
    font-family: "Montserrat", sans-serif; font-weight: 500;
    font-size: 18px; letter-spacing: 1px; line-height: 1.1; color: var(--text-light);
  }
  .contact__title {
    font-family: "Montserrat", sans-serif; font-weight: 400;
    font-size: 12px; letter-spacing: 1px; line-height: 1.3; color: var(--green);
    margin-bottom: 12px;
  }
  .contact__list { list-style: none; }
  .contact__item {
    display: flex; align-items: center; gap: 9px;
    font-size: 12px; line-height: 1.3; margin-bottom: 6px;
  }
  .contact__icon { width: 11px; height: 11px; flex: none; fill: var(--green); }
</style>
</head>
<body>
<main class="canvas">
  <section class="card card-front" aria-label="Card front">
    <div class="card-front__pattern" role="img" aria-label="Repeating tone-on-tone pattern of the brand symbol across the black card"></div>
    <div class="brand">
      <span class="brand__dot"></span>
      <span>Ridgeline<br>Agriculture and Industry</span>
    </div>
  </section>

  <section class="card card-back" aria-label="Card back">
    <div class="brand">
      <span class="brand__dot"></span>
      <span>Ridgeline<br>Agriculture and Industry</span>
    </div>
    <div class="contact">
      <p class="contact__name">YOUR NAME</p>
      <p class="contact__title">JOB TITLE</p>
      <ul class="contact__list">
        <li class="contact__item">
          <svg class="contact__icon" viewBox="0 0 24 24" aria-hidden="true"><path d="M6.6 10.8a15.5 15.5 0 0 0 6.6 6.6l2.2-2.2c.3-.3.7-.4 1-.2 1.1.4 2.3.6 3.6.6.6 0 1 .4 1 1V20c0 .6-.4 1-1 1A17 17 0 0 1 3 4c0-.6.4-1 1-1h3.5c.6 0 1 .4 1 1 0 1.3.2 2.5.6 3.6.1.3 0 .7-.2 1z"/></svg>
          <span>000 000 0000</span>
        </li>
        <li class="contact__item">
          <svg class="contact__icon" viewBox="0 0 24 24" aria-hidden="true"><path d="M2 5h20v14H2z"/><path d="M3 6l9 7 9-7v-.5H3z" fill="#151515"/></svg>
          <span>youremail@xyz.com</span>
        </li>
        <li class="contact__item">
          <svg class="contact__icon" viewBox="0 0 24 24" aria-hidden="true"><circle cx="12" cy="12" r="10"/><path d="M2 12h20M12 2c3 3 3 17 0 20M12 2c-3 3-3 17 0 20" stroke="#151515" stroke-width="1.6" fill="none"/></svg>
          <span>www.yourwebsite.com</span>
        </li>
      </ul>
    </div>
  </section>
</main>
</body>
</html>
```